Bold and modern Raw Manuka Honey label needed

We are needing a new label for one of our honey brands.
Raw Manuka honey has a lot of health benefits and we need a label to look appealing to health minded people but still looking like a jar of honey.
Manuka honey is a very high valued product that we export all over the world so we are looking for a clean and easy to read label as a lot of our customers are foreign and struggle with reading complex labels.
Be creative.... we have a logo and i will add it soon.
I was thinking of adding a silhouette of a bear to go with the Pell Honey name but I'm very open to anything..
Target Market(s)
Health and medical retail shops.
Industry/Entity Type
Health And Wellness
Requirements
Must have
- Brand name is "ambrel"
- Attached is our other label that we are looking at changing as well.
- Company details...
- Pell Honey NZ Limited
- 4/18 Brindle Street
- Central Auckland
- PO Box 41-582
- Auckland
- pellhoneynz@maildrop-nz.com
- www.pellhoneynz-shop.com
Nice to have
- Easy to read.
Should not have
- Hard to read fonts

```html
<!DOCTYPE html>
<html lang="en">
<head>
<meta charset="utf-8">
<title>Manuka Honay 500g Label – Ambrel</title>
<link rel="stylesheet" href="https://fonts.googleapis.com/css2?family=Libre+Baskerville:wght@700&family=Arimo:wght@400;700&family=PT+Sans:wght@400;700&display=swap">
<style>
  :root {
    --pink: #ee2a6e;
    --pink-soft: #f6b3cc;
    --brown: #6b3d12;
    --band-brown: #7a4a16;
    --gold: #c9922f;
    --olive-dark: #2b2a1b;
    --cream: #fffdf6;
    --canvas: #ffffff;
    --frame: #cfcfcf;
    --ink: #222;
  }
  * { box-sizing: border-box; margin: 0; padding: 0; }
  html, body { width: 1200px; height: 1000px; overflow: hidden; background: var(--canvas); }
  .label {
    position: absolute; left: 35px; top: 310px;
    width: 1008px; height: 340px;
    transform: scale(1.12); transform-origin: top left;
    background: var(--pink); border: 2px solid var(--frame);
    font-family: "Arimo", Arial, sans-serif; color: var(--brown);
    overflow: hidden;
  }
  .panel { position: absolute; top: 30px; height: 308px; background: var(--cream); }
  .panel-left { left: 0; width: 330px; border-top-right-radius: 30px; }
  .panel-right { left: 680px; width: 326px; border-top-left-radius: 30px; }
  .panel-centre { left: 330px; width: 350px; top: 0; height: 338px; background: var(--cream); }
  .centre-top { position: absolute; left: 0; top: 0; width: 100%; height: 88px; background: var(--pink); text-align: center; }
  .title {
    font-family: "Libre Baskerville", Georgia, serif; font-weight: 700;
    font-size: 29px; color: #fff4d6; letter-spacing: 0.5px;
    text-shadow: 2px 2px 0 var(--brown);
    padding-top: 16px; line-height: 32px; white-space: nowrap;
  }
  .certified { font-family: "PT Sans", sans-serif; font-size: 15px; color: #fff; line-height: 18px; margin-top: 2px; }
  .premium { font-family: "Arimo", sans-serif; font-weight: 700; font-size: 11px; letter-spacing: 4.5px; color: #fff; line-height: 14px; white-space: nowrap; }
  .brown-band { position: absolute; left: 0; top: 88px; width: 100%; height: 17px; background: var(--band-brown); }
  .flower-hex { position: absolute; left: 95px; top: 108px; width: 160px; height: 160px; }
  .fern-badge { position: absolute; left: 4px; top: 205px; width: 54px; height: 28px; }
  .brand-mark { position: absolute; left: 258px; top: 170px; width: 86px; text-align: center; }
  .brand-mark .dot { display: block; width: 20px; height: 20px; border-radius: 50%; background: var(--brown); margin: 0 auto 6px; }
  .brand-name { font-family: "Libre Baskerville", Georgia, serif; font-weight: 700; font-size: 13px; color: var(--brown); letter-spacing: 0.3px; white-space: nowrap; }
  .weight { position: absolute; left: 276px; top: 226px; font-family: "PT Sans", sans-serif; font-weight: 700; font-size: 22px; color: var(--gold); white-space: nowrap; }
  .company-band { position: absolute; left: 0; top: 262px; width: 100%; height: 76px; background: var(--olive-dark); text-align: center; }
  .company-band .sq { display: block; width: 16px; height: 16px; background: var(--gold); margin: 12px auto 8px; }
  .company-name { font-family: "PT Sans", sans-serif; font-size: 17px; color: #f3efe0; white-space: nowrap; }
  .blossom { position: absolute; width: 22px; height: 22px; border-radius: 50%; background: radial-gradient(circle, #d98aa4 0 25%, var(--pink-soft) 30% 70%, transparent 72%); }
  .intro { position: absolute; left: 40px; top: 40px; width: 240px; font-size: 11px; line-height: 12.5px; color: var(--brown); text-align: justify; }
  .mgo-heading { position: absolute; left: 40px; top: 114px; width: 240px; text-align: center; font-size: 11px; font-weight: 700; }
  .mgo-table { position: absolute; left: 40px; top: 129px; width: 240px; border-collapse: collapse; font-size: 11px; color: var(--ink); }
  .mgo-table th { background: var(--pink); color: #fff; font-weight: 400; height: 17px; }
  .mgo-table td { height: 17px; }
  .mgo-table td:first-child { padding-left: 12px; }
  .mgo-table td:nth-child(2) { text-align: center; }
  .mgo-table td:nth-child(3) { text-align: center; }
  .grade-arrow { position: absolute; left: 233px; top: 170px; width: 10px; height: 46px; }
  .company-details { position: absolute; left: 40px; top: 242px; width: 286px; font-size: 10.5px; line-height: 15.5px; color: var(--brown); white-space: nowrap; }
  .company-details b { font-size: 12px; }
  .company-details .po { position: absolute; left: 166px; top: 0; font-size: 12px; white-space: nowrap; }
  .company-details .small-b { font-size: 10px; }
  .ambrel-foot { position: absolute; left: 230px; top: 290px; font-family: "Libre Baskerville", Georgia, serif; font-weight: 700; font-size: 12px; color: var(--gold); white-space: nowrap; }
  .right-title { position: absolute; left: 68px; top: 54px; font-family: "Libre Baskerville", Georgia, serif; font-weight: 700; font-size: 19px; color: var(--brown); white-space: nowrap; }
  .nutrition { position: absolute; left: 66px; top: 80px; width: 200px; border-collapse: collapse; font-size: 9.5px; color: var(--ink); border: 1.5px solid var(--pink); }
  .nutrition td { border-bottom: 1.5px solid var(--pink); padding: 1px 4px; line-height: 11px; vertical-align: top; }
  .nutrition td + td { border-left: 1.5px solid var(--pink); text-align: center; width: 38px; padding: 1px 2px; }
  .nutrition .head td:first-child { font-size: 10.5px; line-height: 11px; }
  .nutrition .head small { font-size: 8.5px; display: block; line-height: 9.5px; }
  .nutrition .ingredients td { font-size: 9.5px; line-height: 12px; }
  .website { position: absolute; left: 66px; top: 288px; width: 200px; text-align: center; font-size: 11px; color: var(--brown); white-space: nowrap; }
</style>
</head>
<body>
<main class="label">
  <section class="panel panel-left">
    <p class="intro">Ambrel brings you 35 years of quality honay, Our honay are 100% pure natural and nothing added. Honay the way it should bee. Best stored at room temperature and away from direct sunlight.</p>
    <h3 class="mgo-heading">DIETARY MGO CONTENT</h3>
    <table class="mgo-table">
      <tr><th>MGO</th><th>NPA</th><th>GRADE</th></tr>
      <tr><td>MGO30+</td><td>2+</td><td>General</td></tr>
      <tr><td>MGO100+</td><td>5+</td><td></td></tr>
      <tr><td>MGO250+</td><td>10+</td><td></td></tr>
      <tr><td>MGO500+</td><td>15+</td><td></td></tr>
      <tr><td>MGO800+</td><td>20+</td><td>Premium</td></tr>
    </table>
    <svg class="grade-arrow" viewBox="0 0 10 46"><line x1="5" y1="0" x2="5" y2="38" stroke="#000" stroke-width="1.5"/><path d="M1 36 L5 46 L9 36 Z" fill="#000"/></svg>
    <div class="company-details">
      <b>Pell Honey NZ Limited</b><span class="po"><b>PO Box</b> 41-582</span><br>
      4/18 Brindle Street, Auckland Central, New Zealand<br>
      <b>Export ID</b> BUZZ1 <b>PHB</b>2718<br>
      <b class="small-b">Best before</b> January 2019
    </div>
    <span class="ambrel-foot">AMBREL</span>
    <span class="blossom" role="img" aria-label="manuka blossom" style="left:8px;top:150px"></span>
    <span class="blossom" role="img" aria-label="manuka blossom" style="left:285px;top:38px"></span>
    <span class="blossom" role="img" aria-label="manuka blossom" style="left:196px;top:290px"></span>
  </section>

  <section class="panel panel-centre">
    <div class="centre-top">
      <h1 class="title">MANUKA HONAY</h1>
      <p class="certified">CERTIFIED MGO 800+</p>
      <p class="premium">PREMIUM NEW ZEALAND HONAY</p>
    </div>
    <div class="brown-band"></div>
    <svg class="fern-badge" role="img" aria-label="New Zealand origin badge" viewBox="0 0 54 28"><rect x="4" y="2" width="46" height="24" rx="4" fill="#c9922f"/></svg>
    <svg class="flower-hex" role="img" aria-label="manuka flower illustration" viewBox="0 0 160 160">
      <polygon points="80,4 146,42 146,118 80,156 14,118 14,42" fill="#c9922f"/>
      <polygon points="80,14 137,47 137,113 80,146 23,113 23,47" fill="#fff"/>
      <polygon points="80,20 131,50 131,110 80,140 29,110 29,50" fill="#2b2a1b"/>
      <circle cx="80" cy="80" r="44" fill="#f4e6ee"/>
    </svg>
    <div class="brand-mark"><span class="dot"></span><span class="brand-name">AMBREL</span></div>
    <span class="weight">500g</span>
    <div class="company-band"><span class="sq"></span><span class="company-name">Pell Honey NZ Limited</span></div>
    <span class="blossom" role="img" aria-label="manuka blossom" style="left:-6px;top:135px"></span>
  </section>

  <section class="panel panel-right">
    <h2 class="right-title">MANUKA HONAY</h2>
    <table class="nutrition">
      <tr class="head"><td>NUTRITIONAL INFORMATION<small>Servings per package: 50<br>Serving size: 10g</small></td><td>Qty per Serve</td><td>Qty per 100g</td></tr>
      <tr><td>Energy</td><td>132kJ</td><td>1320kJ</td></tr>
      <tr><td>Protein</td><td>&lt;0.1g</td><td>0.4g</td></tr>
      <tr><td>Total Fat<br>&nbsp;- Saturated</td><td>0g<br>0g</td><td>0g<br>0g</td></tr>
      <tr><td>Carbohydrates<br>&nbsp;- Sugars</td><td>8.0g<br>7.8g</td><td>80g<br>78g</td></tr>
      <tr><td>Sodium</td><td>1.2mg</td><td>12mg</td></tr>
      <tr class="ingredients"><td colspan="3">INGREDIENTS: 100% Pure New Zealand Honey, Pollen. Certified MGO 800+</td></tr>
    </table>
    <p class="website">www.pellhoneynz-shop.com</p>
    <span class="blossom" role="img" aria-label="manuka blossom" style="left:30px;top:62px;width:30px;height:30px"></span>
    <span class="blossom" role="img" aria-label="manuka blossom" style="left:280px;top:215px"></span>
    <span class="blossom" role="img" aria-label="manuka blossom" style="left:105px;top:240px"></span>
    <span class="blossom" role="img" aria-label="manuka blossom" style="left:195px;top:312px"></span>
  </section>
  <span class="blossom" role="img" aria-label="manuka blossom" style="left:950px;top:8px"></span>
  <span class="blossom" role="img" aria-label="manuka blossom" style="left:290px;top:-2px"></span>
</main>
</body>
</html>
```